Web Design Project

We need a website design for our marketing agency: clearvane.com.au

We want something that is eye-catching and will wow audiences, yet at the same time it cannot turn-off corporate clients. The website should be highly focused on conversions with numerous call to actions on each page.

We like blue as our primary colour and have a mascot (the spider on the current website)

Target Market(s)

small business owners
small corporations
enterprise level business clients

Industry/Entity Type

Marketing

Requirements
Must have
• must incorporate the agency mascot (the spider on the website)

```html
<!DOCTYPE html>
<html lang="en">
<head>
<meta charset="utf-8">
<title>Clearvane – Digital Marketing</title>
<link rel="stylesheet" href="https://fonts.googleapis.com/css2?family=Bebas+Neue&family=Noto+Sans:wght@400;700&display=swap">
<style>
:root{
  --bg-blue:#5a90aa;
  --texture-light:rgba(255,255,255,.06);
  --texture-dark:rgba(0,40,60,.07);
  --panel-edge:#3f6f86;
  --panel:#ffffff;
  --nav-top:#fbfbfb;
  --nav-bottom:#ececec;
  --nav-line:#d3d3d3;
  --nav-text:#3e3e3e;
  --home:#5d93ad;
  --heading:#5d7480;
  --body:#3b3b3b;
  --link:#2f88b0;
  --rule:#9a9a9a;
  --header-text:#f4f7f8;
}
*{box-sizing:border-box;margin:0;padding:0}
html,body{width:1200px;height:1200px;overflow:hidden}
body{
  position:relative;
  background:
    radial-gradient(ellipse 520px 240px at 560px -40px,rgba(255,255,255,.18),rgba(255,255,255,0) 70%),
    repeating-linear-gradient(45deg,var(--texture-light) 0 1px,transparent 1px 3px),
    repeating-linear-gradient(-45deg,var(--texture-dark) 0 1px,transparent 1px 3px),
    repeating-linear-gradient(0deg,var(--texture-light) 0 1px,transparent 1px 4px),
    var(--bg-blue);
  font-family:"Noto Sans",Verdana,sans-serif;
  color:var(--body);
}
.brand{
  position:absolute;left:155px;top:52px;
  font-family:"Bebas Neue",sans-serif;font-size:44px;letter-spacing:.5px;
  color:var(--header-text);line-height:1;
}
.mascot{
  position:absolute;left:552px;top:16px;width:96px;height:106px;
  border-radius:48px 48px 40px 40px;
  background:radial-gradient(circle at 50% 55%,#c9d3d8,#8c9ca5 70%,#6c7f89);
}
.phone{
  position:absolute;right:155px;top:62px;
  display:flex;align-items:center;gap:10px;
  font-family:"Bebas Neue",sans-serif;font-size:20px;color:var(--header-text);
}
.panel{
  position:absolute;left:144px;top:144px;width:912px;height:1100px;
  background:var(--panel);
  border:4px solid var(--panel-edge);border-bottom:none;
  box-shadow:0 0 6px rgba(0,0,0,.2);
}
.nav{
  height:46px;border-bottom:1px solid var(--nav-line);
  background:linear-gradient(var(--nav-top),var(--nav-bottom));
  display:flex;align-items:center;padding-left:10px;gap:4px;
}
.nav a{
  font-size:11px;color:var(--nav-text);text-decoration:none;
  padding:5px 8px;border-radius:3px;margin-right:4px;
}
.nav a.current{background:var(--home);color:#fff;box-shadow:inset 0 0 0 1px #4a7e97}
.service{position:absolute;top:66px;width:277px;text-align:center}
.service .tile{
  width:111px;height:113px;margin:0 auto;border-radius:8px;
  background:linear-gradient(#f3f3f3,#d8d8d8);
  box-shadow:0 3px 4px rgba(0,0,0,.25),inset 0 0 0 1px #fff;
  position:relative;
}
.tile .art{position:absolute;inset:14px;border-radius:50%}
.h{
  font-family:"Bebas Neue",sans-serif;color:var(--heading);
  font-size:28px;line-height:1;font-weight:400;
}
.service .h{margin-top:31px}
.service p,.feature p{
  font-size:10.5px;line-height:18.5px;text-align:justify;margin-top:8px;
}
.rule{position:absolute;left:20px;width:864px;border-top:1px dotted var(--rule)}
.feature{position:absolute;left:174px;width:712px}
.feature p{margin-top:6px}
.feature p + p{margin-top:9px}
.feature.bold p{font-weight:700;font-size:10.3px}
.feature a{color:var(--link);text-decoration:none;font-weight:400}
.chart-art{
  position:absolute;left:26px;top:414px;width:120px;height:104px;border-radius:6px;
  background:linear-gradient(90deg,#f59a35 0 30%,#5b5cf0 30% 62%,#22cc22 62% 100%);
  opacity:.85;
}
.seo-art{
  position:absolute;left:22px;top:645px;width:135px;height:105px;
  background:linear-gradient(135deg,#f2f2f2,#cfcfcf);border-radius:6px;
}
</style>
</head>
<body>
  <div class="brand">Clearvane</div>
  <div class="mascot" role="img" aria-label="Clearvane spider mascot illustration"></div>
  <div class="phone">
    <svg width="16" height="12" viewBox="0 0 16 12" aria-hidden="true"><path d="M1 4c0-2 3-3 7-3s7 1 7 3v1h-4V4H5v1H1z M4 6h8l2 5H2z" fill="#fff"/></svg>
    (+617) 3000 4821
  </div>

  <main class="panel">
    <nav class="nav">
      <a class="current" href="#">Home</a>
      <a href="#">Services</a>
      <a href="#">Blog</a>
      <a href="#">SEO Pricing</a>
      <a href="#">SEM</a>
      <a href="#">About Clearvane</a>
      <a href="#">Contact Clearvane</a>
    </nav>

    <section class="service" style="left:18px">
      <div class="tile"><div class="art" role="img" aria-label="Dartboard with a dart in the bullseye" style="background:radial-gradient(circle,#b8bfc3,#8e979c)"></div></div>
      <h2 class="h">Online Ad Management</h2>
      <p>Need highly targeted traffic right now? Then let us help! We have a whole range of online advertising solutions, from Searchly Ads to Friendwall Ads to interactive banner Ads. Ad copy, creatives design &amp; conversion optimization – we can handle everything and get you the highest ROI for your ad dollar.</p>
    </section>
    <section class="service" style="left:314px">
      <div class="tile"><div class="art" role="img" aria-label="Blue globe with network nodes" style="background:radial-gradient(circle,#bcd6ea,#86aecb)"></div></div>
      <h2 class="h">SEO Packages</h2>
      <p>Drive quality traffic to your business and boost your revenue. We offer high quality SEO packages at competitive rates with GUARANTEED results. Whether you’re a local business or a national enterprise, we can help your business grow.</p>
    </section>
    <section class="service" style="left:609px">
      <div class="tile"><div class="art" role="img" aria-label="Blue and green speech bubbles" style="background:linear-gradient(120deg,#7aa7ec,#6fd9aa)"></div></div>
      <h2 class="h">Social Media</h2>
      <p>Need to engage your target market? Want build your brand to create a loyal base of supporters for your business? Then social media is your solution. We can advise which social media options are right for your business – and there are way more options than just Friendwall and Chirpline!</p>
    </section>

    <div class="rule" style="top:379px"></div>

    <div class="chart-art" role="img" aria-label="Illustration of glossy orange, blue and green bars with a magnifying glass"></div>
    <section class="feature" style="top:414px">
      <h2 class="h">Clearvane Digital Marketing</h2>
      <p>Online marketing channels are a major factor almost any business. Clearvane is a digital marketing agency focused on results and ROI. Whether its search engine optimisation with our advanced SEO services or Pay-Per-Click search engine marketing (SEM) – we are here to help you achieve your business goals with our range of results-oriented marketing solutions.</p>
      <p>Clearvane accepts clients big and small – whether you’re an international corporation needing to boost seasonal sales with multi-platform online ad campaign, a government department trying to raise public awareness, or an electrical contractor needing SEO Brisbane. We are a digital agency that actually cares about your business and would love to help you grow.</p>
    </section>

    <div class="rule" style="top:610px"></div>

    <div class="seo-art" role="img" aria-label="Stacked white cubes spelling SEO"></div>
    <section class="feature bold" style="top:645px">
      <h2 class="h">Search Engine Optimisation</h2>
      <p>A website without traffic is useless. Traffic is the commodity of the internet: driving information &amp; business in our online economy. You don’t need to have an online store to benefit from search engine optimisation. Studies show that almost 66% of purchases (offline and online together) start with the consumer looking for information on a search engine.</p>
      <p style="margin-top:18px">Ignoring your search visibility and rankings can hurt the growth and success of your business. Business today cannot afford online obscurity – you may as well send customers to your competitors. We can help your business increase its revenue and reach via a range of online marketing channels – <a href="#">get in contact now</a> to find out how. Clearvane offers the best international, national and Brisbane SEO services.</p>
    </section>
  </main>
</body>
</html>
```